Life Coach business needs a website design

I would like to get support in creating a website design. I will be starting a business as a life coach and I would like to start with something basic, but chic. It will be mainly a blog for now, but then I would like to start adding videos and hopefully podcast in the future. I took professional pictures of myself that I would like to include as a cover page. My main goal with this website is to capture the right audience by connecting with them through my mission, which is to embrace their inner greatness. I want to provide a sense of love, courage and authenticity when they open my website. I have a domain in Brickloft called :"Unfold the hidden melody". I would be happy to discuss more of the details over the phone.

Target Market(s)

Young Adults (25-35)

Number of Pages Required

4 page

Colors

Designer to choose colors to be used in the design.

Requirements
Must have
• I am looking for a similar layout and vibe to these websites: https://tessawhitcombe.net/meet-tessa/
• https://www.ninaculvane.com
• My home page will include: About, Blog, Podcast, Subscribe.. (We can add icons of snapreel, vidloom and Tackboard)
• I would like to have my name in the middle (Ondra), and include a note next to my picture "Your life is like a blank canvas and only you have the power to transform it into masterpiece. Take a chance and unfold the hidden melody" O.K.

```html
<!DOCTYPE html>
<html lang="en">
<head>
<meta charset="utf-8">
<title>Ondra — Life Coach</title>
<link href="https://fonts.googleapis.com/css2?family=Montserrat:ital,wght@0,300;0,400;0,500;0,600;0,700;1,400;1,700&display=swap" rel="stylesheet">
<style>
:root{
  --pink:#f38b8b;
  --pink-soft:#fdeeee;
  --grey-dark:#5f5f5f;
  --grey-hero:#6a6a6a;
  --grey-light:#f1f1f1;
  --ink:#3a3a3a;
  --muted:#8a8a8a;
  --white:#ffffff;
}
*{box-sizing:border-box;margin:0;padding:0}
html,body{width:1200px;height:3324px;overflow:hidden}
body{font-family:'Montserrat',sans-serif;color:var(--ink);background:var(--white);position:relative}
section,header,footer{position:absolute;left:0;width:1200px}
.abs{position:absolute}

/* hero */
.hero{top:0;height:572px;background:var(--grey-hero)}
.hero-photo{right:150px;top:0;width:420px;height:572px;background:radial-gradient(ellipse at 55% 40%,#c89580 0%,#7a5648 38%,#3b2a25 70%,#6a6a6a 100%)}
.brand{left:160px;top:30px;width:140px;color:var(--pink);font-size:14px;font-weight:600;line-height:1.25;letter-spacing:.3px}
.nav{left:320px;top:50px;display:flex;gap:30px;font-size:11px;font-weight:600;color:var(--white);letter-spacing:1px}
.nav .active{border-bottom:2px solid var(--pink);padding-bottom:4px}
.social{display:flex;gap:8px}
.social span{width:14px;height:14px;border-radius:50%;background:var(--white);opacity:.85;display:block}
.hero .social{left:975px;top:48px}
.hero-hi{left:160px;top:250px;font-size:78px;font-weight:700;color:var(--white);font-style:italic;line-height:1}
.hero-name{left:160px;top:360px;font-size:40px;font-weight:600;color:var(--white);line-height:1.1}
.hero-text{left:160px;top:425px;width:330px;font-size:12px;line-height:1.7;color:#e8e8e8}
.btn{display:inline-block;font-size:10px;font-weight:600;letter-spacing:1px;border-radius:20px;padding:11px 30px}
.btn-pink{background:var(--pink);color:var(--white)}
.hero .btn{left:160px;top:500px;position:absolute}

/* about quote */
.about{top:572px;height:438px;background:var(--pink-soft)}
.about-photo{left:40px;top:0;width:360px;height:438px;background:linear-gradient(180deg,#f7e7e5 0%,#c9a99a 35%,#6d7f9e 70%,#f5e9e8 100%)}
.quote-box{left:470px;top:130px;width:620px;height:210px;border:2px solid #f4b5b5}
.quote-text{left:510px;top:165px;width:540px;text-align:center;font-style:italic;font-size:18px;line-height:1.6;color:#7a6d6d}
.quote-name{left:470px;top:318px;width:620px;text-align:center;line-height:1}
.quote-name strong{display:inline-block;background:var(--pink-soft);padding:0 18px;color:var(--pink);font-size:30px;font-weight:500}
.quote-role{left:470px;top:360px;width:620px;text-align:center;font-size:12px;font-weight:600;color:var(--ink)}
.quote-sub{left:470px;top:380px;width:620px;text-align:center;font-size:9px;color:var(--muted)}

/* help */
.help{top:1010px;height:530px;background:var(--white)}
.help h2{left:180px;top:40px;width:330px;font-size:24px;font-weight:500;line-height:1.35;position:absolute}
.help-text{left:180px;top:125px;width:260px;font-size:11px;line-height:1.9;color:var(--muted)}
.slider{left:180px;top:300px;width:260px;height:2px;background:#ccc}
.slider::before{content:"";position:absolute;left:0;top:-2px;width:12px;height:6px;background:var(--ink)}
.slider::after{content:"";position:absolute;left:14px;top:-1px;width:110px;height:4px;background:var(--ink)}
.help-block{left:480px;top:130px;width:392px;height:280px;background:#e2e2e2}
.help-photo{left:512px;top:170px;width:520px;height:320px;background:linear-gradient(180deg,#cf9a86 0%,#f2b58a 40%,#e48a4a 60%,#4a3a3a 100%)}

/* posts */
.posts{top:1540px;height:600px;background:var(--pink-soft)}
.section-title{width:1200px;text-align:center;font-size:24px;font-weight:500;position:absolute;left:0}
.posts .section-title{top:60px}
.card{width:260px;height:390px;background:var(--white);top:150px;position:absolute}
.card-date{position:absolute;left:0;top:2px;font-size:9px;font-weight:600;color:var(--ink)}
.card-img{position:absolute;left:0;top:22px;width:260px;height:200px}
.card h3{position:absolute;left:0;top:240px;width:250px;font-size:12px;font-weight:600;line-height:1.5}
.card p{position:absolute;left:0;top:285px;width:250px;font-size:10px;line-height:1.6;color:var(--muted)}
.card-more{position:absolute;right:4px;bottom:14px;width:18px;height:18px;background:var(--pink);opacity:.7}

/* cta */
.cta{top:2140px;height:180px;background:var(--grey-dark)}
.cta h2{position:absolute;width:1200px;top:55px;text-align:center;color:var(--white);font-size:22px;font-weight:600}
.btn-outline{position:absolute;left:540px;top:110px;width:120px;text-align:center;border:1.5px solid var(--white);color:var(--white);padding:9px 0}

/* testimonials */
.testimonials{top:2320px;height:552px;background:var(--grey-light)}
.testimonials .section-title{top:45px}
.lead{position:absolute;width:1200px;top:102px;text-align:center;font-size:11px;color:var(--muted)}
.tcard{position:absolute;top:185px;width:280px;height:200px;background:var(--white);border-radius:4px;text-align:center}
.tcard.featured{border:2px solid var(--pink)}
.tcard .qmark{position:absolute;left:126px;top:-14px;width:28px;height:28px;border-radius:50%;background:#c9c9c9;color:var(--white);font-size:20px;line-height:34px;font-weight:700}
.tcard.featured .qmark{background:var(--pink)}
.tcard p{position:absolute;left:25px;top:32px;width:230px;font-size:10px;line-height:1.7;color:var(--muted)}
.avatar{position:absolute;top:360px;width:64px;height:64px;border-radius:50%;background:linear-gradient(135deg,#9a8478,#4c3f3a);border:3px solid var(--white)}
.tname{position:absolute;top:438px;width:280px;text-align:center;font-size:10px;font-weight:600;letter-spacing:.5px}

/* newsletter */
.newsletter{top:2872px;height:220px;background:var(--grey-dark)}
.newsletter h2{position:absolute;width:1200px;top:48px;text-align:center;color:var(--white);font-size:20px;font-weight:500}
.field{position:absolute;top:110px;width:200px;height:36px;background:var(--white);border-radius:2px;font-size:10px;color:var(--muted);padding:12px 12px}
.field.submit{background:var(--pink);color:var(--white);text-align:center;font-weight:600;letter-spacing:1px}
.consent{position:absolute;left:160px;top:162px;font-size:9px;color:#dcdcdc;display:flex;align-items:center;gap:8px}
.consent i{width:10px;height:10px;border:1px solid #ddd;display:block}

/* footer */
.site-footer{top:3092px;height:232px;background:var(--white)}
.ficon{position:absolute;top:48px;width:48px;height:48px;border-radius:50%;background:#d9d9d9;display:flex;align-items:center;justify-content:center}
.finfo{position:absolute;top:46px;font-size:10px;line-height:1.6;color:var(--muted)}
.finfo .lbl{color:var(--pink);font-weight:600}
.phone-big{position:absolute;left:852px;top:56px;font-size:26px;font-weight:400;color:var(--ink)}
.fnav{position:absolute;width:1200px;top:150px;display:flex;justify-content:center;gap:24px;font-size:9px;font-weight:600;letter-spacing:1px}
.copy{position:absolute;left:160px;top:186px;font-size:8px;color:var(--muted)}
.site-footer .social{position:absolute;left:985px;top:182px}
.site-footer .social span{background:#bdbdbd}
.rule{position:absolute;left:160px;top:140px;width:880px;height:1px;background:#eee}
</style>
</head>
<body>

<header class="hero">
  <div class="abs hero-photo" role="img" aria-label="Portrait of the coach smiling, long dark curly hair"></div>
  <div class="abs brand">Unfold the<br>hidden melody</div>
  <nav class="abs nav"><span class="active">HOME</span><span>ABOUT</span><span>PODCAST</span><span>BLOG</span><span>CONTACT</span></nav>
  <div class="abs social"><span></span><span></span><span></span></div>
  <h1 class="abs hero-hi">Hi !</h1>
  <p class="abs hero-name">I'M Ondra</p>
  <p class="abs hero-text">Gentle guidance for anyone ready to grow, heal and shine with calm courage every single day.</p>
  <a class="btn btn-pink">LEARN MORE</a>
</header>

<section class="about">
  <div class="abs about-photo" role="img" aria-label="Full-length photo of the coach in a floral skirt"></div>
  <div class="abs quote-box"></div>
  <p class="abs quote-text">"Your life is like a blank canvas and only you have the power to transform it into masterpiece. Take a chance and unfold the hidden melody" O.K.</p>
  <div class="abs quote-name"><strong>Ondra</strong></div>
  <p class="abs quote-role">Life Coach</p>
  <p class="abs quote-sub">Guiding you to your truest self</p>
</section>

<section class="help">
  <h2>Let me help you start<br>living a spiritual life!</h2>
  <p class="abs help-text">Slow down, breathe and listen to what your heart has been saying. Together we build daily rituals, honest goals and kind habits that bring love, courage and truth into your work, your home and every quiet moment you share.</p>
  <div class="abs slider"></div>
  <div class="abs help-block"></div>
  <div class="abs help-photo" role="img" aria-label="Person meditating on a rock at sunset"></div>
</section>

<section class="posts">
  <h2 class="section-title">Recent Posts</h2>
  <article class="card" style="left:180px">
    <span class="card-date">Thursday May 6th, 2021</span>
    <div class="card-img" role="img" aria-label="Blog photo of the coach outdoors" style="background:linear-gradient(160deg,#d7c2b0,#6e5247)"></div>
    <h3>Donec vestibulum luctus felis, sit amet tincidunt</h3>
    <p>Small daily choices shape a bright life. Here is how to begin today with care.</p>
    <span class="card-more"></span>
  </article>
  <article class="card" style="left:470px">
    <span class="card-date">Thursday May 6th, 2021</span>
    <div class="card-img" role="img" aria-label="Blog photo of the coach in a light dress" style="background:linear-gradient(160deg,#c9b7ae,#5a4640)"></div>
    <h3>Donec vestibulum luctus felis, sit amet tincidunt</h3>
    <p>Courage grows when we say yes to ourselves. Three simple steps to try this week.</p>
    <span class="card-more"></span>
  </article>
  <article class="card" style="left:760px">
    <span class="card-date">Thursday May 6th, 2021</span>
    <div class="card-img" role="img" aria-label="Blog photo of the coach on a beach" style="background:linear-gradient(180deg,#cde0ea,#e9d6cc 60%,#8a6a5c)"></div>
    <h3>Donec vestibulum luctus felis, sit amet tincidunt</h3>
    <p>Rest is not a reward, it is a need. Learn to pause and hear your own voice.</p>
    <span class="card-more"></span>
  </article>
</section>

<section class="cta">
  <h2>Feel spiritually connected every day!</h2>
  <a class="btn btn-outline">GET STARTED</a>
</section>

<section class="testimonials">
  <h2 class="section-title">Testimonials</h2>
  <p class="lead">Donec vestibulum luctus felis, sit amet tincidunt lorem tincidunt a.</p>
  <div class="tcard" style="left:160px"><span class="qmark">“</span><p>Working with Ondra opened my eyes. I feel calmer, braver and far more honest with myself. Each session left me lighter and ready to take real steps forward.</p></div>
  <div class="tcard featured" style="left:460px"><span class="qmark">“</span><p>I came in lost and left with a clear plan. Her warmth and patience helped me trust my own choices again. I am truly grateful for every talk we shared.</p></div>
  <div class="tcard" style="left:760px"><span class="qmark">“</span><p>The rituals she taught me are now part of every morning. My stress is lower and my joy is higher. I would suggest her to anyone who feels stuck.</p></div>
  <div class="avatar" style="left:268px" role="img" aria-label="Client portrait"></div>
  <div class="avatar" style="left:568px" role="img" aria-label="Client portrait"></div>
  <div class="avatar" style="left:868px" role="img" aria-label="Client portrait"></div>
  <p class="tname" style="left:160px">ARLO PENWICK</p>
  <p class="tname" style="left:460px">THEO MARSDEN</p>
  <p class="tname" style="left:760px">THEO MARSDEN</p>
</section>

<section class="newsletter">
  <h2>Signup For Our Newsletter</h2>
  <div class="field" style="left:160px">First Name</div>
  <div class="field" style="left:400px">Last Name</div>
  <div class="field" style="left:640px">Email</div>
  <div class="field submit" style="left:880px;width:160px">SUBMIT</div>
  <div class="consent"><i></i>I agree to receive weekly notes from Unfold the hidden melody.</div>
</section>

<footer class="site-footer">
  <div class="ficon" style="left:160px"><svg width="18" height="22" viewBox="0 0 18 22"><path d="M9 1a7 7 0 0 0-7 7c0 5 7 13 7 13s7-8 7-13a7 7 0 0 0-7-7z" fill="#fff"/><circle cx="9" cy="8" r="2.5" fill="#d9d9d9"/></svg></div>
  <p class="finfo" style="left:222px"><span class="lbl">Visit</span><br>Studio 4, 22 Larch Lane<br>Hollowmere, HM 3012<br>Open Mon to Fri</p>
  <div class="ficon" style="left:470px"><svg width="22" height="16" viewBox="0 0 22 16"><rect x="1" y="1" width="20" height="14" rx="1" fill="#fff"/><path d="M1 2l10 7 10-7" stroke="#d9d9d9" stroke-width="1.5" fill="none"/></svg></div>
  <p class="finfo" style="left:532px;top:64px">hello@unfoldmelody.net</p>
  <div class="ficon" style="left:790px"><svg width="20" height="20" viewBox="0 0 20 20"><path d="M5 1l3 4-2 2c1 3 3 5 6 6l2-2 4 3-2 4C8 18 2 12 1 3z" fill="#fff"/></svg></div>
  <p class="phone-big">04 26 83 19 57</p>
  <div class="rule"></div>
  <nav class="fnav"><span>HOME</span><span>ABOUT</span><span>PODCAST</span><span>BLOG</span><span>CONTACT</span></nav>
  <p class="copy">© 2021 Unfold the hidden melody. All rights kept.</p>
  <div class="social"><span></span><span></span><span></span></div>
</footer>

</body>
</html>
```